Church Rivers of Morning Gospel Booklet Design

We need a booklet designed that we will be printing to hand out in our community. Wording for each page will be provided and we need graphic design to produce the layouts in a format ready for print. Booklet will be 4.75" x 4.75" square and a total of 12 pages: 1 cover page front, 1 cover page back, 10 inside pages some of which will be full spread across 2 pages.

Target Market(s)

English speaking Westerners

Industry/Entity Type

Religious

Font styles to use
Serif

Colors
ffffff
85abd2
0292cd
33b8a4
5c5c5c

Requirements
Must have
• Minimalist design with clean look described in attached document
Nice to have
• Aesthetically pleasing graphics, crisp fonts, excellent turn around times
Should not have
• Effeminate design, busy look with too much graphic and text

```html
<!DOCTYPE html>
<html lang="en">
<head>
<meta charset="utf-8">
<title>Rivers of Morning — Gospel Booklet, Pages 6–7</title>
<link rel="stylesheet" href="https://fonts.googleapis.com/css2?family=Source+Serif+4:ital,opsz,wght@0,8..60,400;1,8..60,400&display=swap">
<style>
  :root {
    --paper: #ffffff;
    --ink: #454545;
    --ink-soft: #5c5c5c;
    --dusk-dark: #2a2119;
    --dusk-amber: #b8692e;
    --dusk-glow: #e39a45;
    --sky-gold: #d8b865;
    --sky-light: #f1e2b0;
    --sky-deep: #9c8448;
  }
  * { box-sizing: border-box; margin: 0; padding: 0; }
  html, body {
    width: 1200px;
    height: 600px;
    overflow: hidden;
    background: var(--paper);
  }
  .spread {
    position: relative;
    width: 1200px;
    height: 600px;
    background: var(--paper);
    font-family: "Source Serif 4", Georgia, serif;
    color: var(--ink);
  }
  .page { position: absolute; top: 0; width: 600px; height: 600px; }
  .page--left { left: 0; }
  .page--right { left: 600px; }

  .body-copy {
    position: absolute;
    font-size: 18px;
    white-space: nowrap;
  }
  .body-copy .line { display: block; }
  .page--left .body-copy { left: 75px; top: 82px; line-height: 22.7px; }
  .page--right .body-copy { left: 68px; top: 325px; line-height: 21.2px; }

  .photo { position: absolute; display: block; }
  .photo--struggle {
    left: 186px; top: 289px; width: 233px; height: 233px;
    background: linear-gradient(160deg, var(--dusk-glow) 0%, var(--dusk-amber) 45%, var(--dusk-dark) 100%);
  }
  .photo--praise {
    left: 189px; top: 71px; width: 233px; height: 233px;
    background: linear-gradient(180deg, var(--sky-gold) 0%, var(--sky-light) 50%, var(--sky-gold) 85%, var(--sky-deep) 100%);
  }

  .scripture {
    position: absolute;
    left: 100px; top: 482px;
    list-style: none;
    font-style: italic;
    font-size: 14.6px;
    line-height: 17.8px;
    color: var(--ink-soft);
    white-space: nowrap;
  }
  .scripture li { position: relative; }
  .scripture .line { display: block; }
  .scripture li::before {
    content: "";
    position: absolute; left: -10px; top: 7px;
    width: 5px; height: 5px; border-radius: 50%;
    background: var(--ink-soft);
  }

  .folio {
    position: absolute;
    top: 537px;
    font-style: italic;
    font-size: 15px;
    color: var(--ink-soft);
  }
  .page--left .folio { left: 59px; }
  .page--right .folio { left: 542px; }
</style>
</head>
<body>
<main class="spread">
  <section class="page page--left">
    <p class="body-copy">
      <span class="line">This alienation from God is evident in a myriad</span>
      <span class="line">of ways including poverty, crime, conflict in our</span>
      <span class="line">relationships, and our internal struggles. But worse,</span>
      <span class="line">when we die, we must face the consequences for</span>
      <span class="line">our rejection of God by spending eternity in hell -</span>
      <span class="line">a lake of fire created by God as the place where our</span>
      <span class="line">treason is brought to justice.</span>
    </p>
    <div class="photo photo--struggle" role="img" aria-label="Photograph of a person in distress at sunset"></div>
    <span class="folio">6</span>
  </section>

  <section class="page page--right">
    <div class="photo photo--praise" role="img" aria-label="Photograph of a person with arms raised under a golden sky"></div>
    <p class="body-copy">
      <span class="line">But God does not want you to pay for your own</span>
      <span class="line">sins. God loves us so much he sent his only son</span>
      <span class="line">to save us. Jesus Christ died on the cross to serve</span>
      <span class="line">our sentence for our rebellion against God and</span>
      <span class="line">rose again on the third day. Since Christ paid our</span>
      <span class="line">full penalty, we can be completely forgiven and</span>
      <span class="line">reconciled to God.</span>
    </p>
    <ul class="scripture">
      <li>
        <span class="line">“For God so loved the world that he sent his one and</span>
        <span class="line">only son that whosoever believes in him will not perish</span>
        <span class="line">but have eternal life.” (John 3:16)</span>
      </li>
    </ul>
    <span class="folio">7</span>
  </section>
</main>
</body>
</html>
```